Dentistry

Dentist's personal business card. No logo needed. The card shoul deliver the massage of reliability, professionalism, experience.
Please ad the full brief of the project: down the line it says: the winning look should be precise and pristine NO pictures of Teeth, smiles, instruments etc.

The details to be desplaid are:
Dr. Rob Valdoni
Doctor of Dental Surgery
PHD
Web. Www.drvaldoni.com
Email. Rob@drvaldoni.com
Tel 07731482590
Surgery address. 27Bharwick road London SW4 7QN UK
82 Fenwyn Row London SW3 2HT. Uk

Reason: Decided to make the payment unrefundable in order to get more designers involved.

Requirements
Should not have
• Logo, teeth, smile any sort of instruments.

```html
<!DOCTYPE html>
<html lang="en">
<head>
<meta charset="utf-8">
<title>Dr. Rob Valdoni – Business Card</title>
<link rel="stylesheet" href="https://fonts.googleapis.com/css2?family=Open+Sans:wght@300;400;600;700&display=swap">
<style>
  :root {
    --card-red: #ed2129;
    --shadow-red: #a3161b;
    --ink-white: #ffffff;
    --icon-dark: #1c1c1c;
  }
  * { box-sizing: border-box; margin: 0; padding: 0; }
  html, body {
    width: 1200px; height: 667px; overflow: hidden;
    background: var(--card-red);
    font-family: "Open Sans", "Segoe UI", sans-serif;
    color: var(--ink-white);
  }
  .card {
    position: relative; width: 1200px; height: 667px;
    background: var(--card-red); overflow: hidden;
  }
  .header-band {
    position: absolute; left: 0; top: 0; width: 1200px; height: 303px;
    background: var(--card-red);
    display: flex; align-items: center; justify-content: center;
    z-index: 2;
  }
  .band-shadow {
    position: absolute; left: -40px; top: 296px; width: 1280px; height: 44px;
    background: radial-gradient(ellipse 50% 50% at 50% 20%, rgba(120,10,14,0.75) 0%, rgba(160,20,25,0.45) 45%, rgba(237,33,41,0) 100%);
    z-index: 1;
  }
  .title {
    font-size: 45px; font-weight: 300; letter-spacing: 0.2px; white-space: nowrap;
    margin-top: -14px;
  }
  .title .name { font-weight: 600; }
  .contact {
    position: absolute; display: flex; align-items: center;
  }
  .icon {
    position: absolute; width: 48px; height: 48px; border-radius: 50%;
    background: var(--ink-white);
    display: flex; align-items: center; justify-content: center;
  }
  .icon svg { width: 26px; height: 26px; }
  .text {
    position: absolute; font-size: 26px; font-weight: 300; line-height: 37px; white-space: nowrap;
  }
  .text .label { font-weight: 600; }
</style>
</head>
<body>
<div class="card">
  <header class="header-band">
    <h1 class="title"><span class="name">Dr. Rob Valdoni</span> - Doctor of Dental Surgery PHD</h1>
  </header>
  <div class="band-shadow"></div>

  <!-- address -->
  <div class="icon" style="left:44px; top:408px;">
    <svg viewBox="0 0 24 24"><path fill="var(--icon-dark)" d="M12 3 2 12h3v9h5v-6h4v6h5v-9h3z"/></svg>
  </div>
  <p class="text" style="left:123px; top:398px;"><span class="label">Address:</span> 27Bharwick road London SW4<br>7QN UK 82 Fenwyn Row London SW3 2HT. Uk</p>

  <!-- email -->
  <div class="icon" style="left:726px; top:408px;">
    <svg viewBox="0 0 24 24"><path fill="var(--icon-dark)" d="M2 10 12 3l10 7v10H2z"/><path fill="#fff" d="M4 10.5 12 16l8-5.5V19H4z"/><path fill="none" stroke="var(--icon-dark)" stroke-width="1.4" d="M4 19l6-5M20 19l-6-5"/></svg>
  </div>
  <p class="text" style="left:831px; top:414px;"><span class="label">Email:</span> Rob@drvaldoni.com</p>

  <!-- phone -->
  <div class="icon" style="left:44px; top:556px;">
    <svg viewBox="0 0 24 24"><path fill="var(--icon-dark)" d="M6.6 3.5 9 6.8 7.6 9c.9 2.6 3 4.8 5.5 5.8l2.1-1.5 3.3 2.4-1.6 3.2C10.2 19 4.6 13.3 3.5 6.4z"/><path fill="none" stroke="var(--icon-dark)" stroke-width="1.3" d="M14 4.5a6 6 0 0 1 5.5 5.5M14 7.5a3 3 0 0 1 2.6 2.6"/></svg>
  </div>
  <p class="text" style="left:123px; top:565px;"><span class="label">Ph:</span> 07731482590</p>

  <!-- web -->
  <div class="icon" style="left:726px; top:556px;">
    <svg viewBox="0 0 24 24"><circle cx="12" cy="12" r="10" fill="var(--icon-dark)"/><path fill="none" stroke="#fff" stroke-width="1.6" d="M3 9.5c5-2 13-2 18 0M2.5 14c6-2.5 13-2.5 19 0M5 18.5c4-2 10-2 14 0"/></svg>
  </div>
  <p class="text" style="left:831px; top:558px;">www.drvaldoni.com</p>
</div>
</body>
</html>
```